Photography business - business card design quick turn around

Create a business card design for me please. I actually need the final design back before the end of Sunday 13th May 7pm GMT. Sorry for the short notice.

Photoshop artwork template uploaded with artwork guidelines including printer profiles and other mandatory specifications. Only one side of the business card is required as the other side will be an image.

The design is required as an unflattened PSD file so that I can edit the text if I need to.

My brand colours are white and the teal you see in the logo. Occasionally I also use a dark grey on my website (I don't mind the shade of grey as appreciate grey on teal would be a different grey, to the grey I use on white on the website, so just use a shade of grey that matches). Font can be as the font for the logo or if you prefer I am open to another sans serif, easily legible font. Ideally font size will be 12+.Please do not use capital letters for text. I prefer everything to be lower case, if possible.

Thank you.

Nell

Target Market(s)

Other business owners who may refer me and families

Industry/Entity Type

Photographer

Contact Information for Business Card

Silver Kettle Photography Logo
Sub text: family portraiture, captured with love

Contact information, ideally using simple icons to represent email / website / facebook / instagram / pinterest

email: nell@silverkettlephotography.co.uk
website: silverkettlephotography.co.uk
facebook: @silverkettlephotography
pinterest: pinterest.com/silverkettlepho
instagram: @silverkettle_photography
mobile/telephone: 07931462097

If there is too much text then please drop the instagram and pinterest information.

Font styles to use
Sans Serif

Colors
33b8a4

Requirements
Must have
• Logo
• Contact details as listed above
• sub text
Nice to have
• Instagram and Pinterest contact details
• Nice to have icons to represent website / phone / facebook etc followered by the handle where relevant

```html
<!DOCTYPE html>
<html lang="en">
<head>
<meta charset="utf-8">
<title>Silver Kettle Photography – business card</title>
<link rel="stylesheet" href="https://fonts.googleapis.com/css2?family=Quicksand:wght@500;700&display=swap">
<style>
  :root {
    --teal: #33b8a4;
    --grey: #6b6f70;
    --card: #ffffff;
    --backdrop: #e9ebea;
  }
  html, body {
    margin: 0;
    width: 900px;
    height: 1200px;
    overflow: hidden;
    background: var(--backdrop);
    font-family: "Quicksand", sans-serif;
  }
  .business-card {
    position: absolute;
    left: 40px;
    top: 323px;
    width: 820px;
    height: 554px;
    background: var(--card);
    border-radius: 28px;
    box-shadow: 0 10px 30px rgba(0,0,0,0.12);
    overflow: hidden;
  }
  .brand {
    position: absolute;
    left: 40px;
    top: 160px;
    width: 290px;
    text-align: center;
  }
  .brand-mark {
    display: block;
    width: 70px;
    height: 70px;
    margin: 0 auto 18px;
    border-radius: 50%;
    background: var(--teal);
  }
  .brand-name {
    margin: 0;
    font-weight: 700;
    font-size: 30px;
    line-height: 1.15;
    color: var(--teal);
  }
  .divider {
    position: absolute;
    left: 352px;
    top: 170px;
    width: 2px;
    height: 236px;
    background: var(--teal);
  }
  .contact-list {
    position: absolute;
    left: 372px;
    top: 168px;
    margin: 0;
    padding: 0;
    list-style: none;
  }
  .contact-item {
    display: flex;
    align-items: center;
    height: 40px;
    font-weight: 500;
    font-size: 19px;
    color: var(--teal);
    white-space: nowrap;
  }
  .contact-icon {
    flex: none;
    width: 22px;
    height: 22px;
    margin-right: 12px;
  }
  .tagline {
    position: absolute;
    left: 0;
    right: 0;
    top: 466px;
    margin: 0;
    text-align: center;
    font-weight: 500;
    font-size: 20px;
    color: var(--grey);
  }
</style>
</head>
<body>
  <section class="business-card">
    <div class="brand">
      <span class="brand-mark"></span>
      <p class="brand-name">Silver Kettle<br>Photography</p>
    </div>

    <div class="divider"></div>

    <ul class="contact-list">
      <li class="contact-item">
        <svg class="contact-icon" viewBox="0 0 22 22" aria-hidden="true">
          <circle cx="11" cy="11" r="11" fill="var(--teal)"/>
          <path d="M7.5 6.5c.6-.6 1.4-.4 1.7.2l.9 1.8c.2.5.1 1-.3 1.3l-.6.5c.5 1.1 1.4 2 2.5 2.5l.5-.6c.3-.4.8-.5 1.3-.3l1.8.9c.6.3.8 1.1.2 1.7l-.7.7c-1.6 1.2-7.8-4.6-7.9-7.5z" fill="#fff"/>
        </svg>07931462097
      </li>
      <li class="contact-item">
        <svg class="contact-icon" viewBox="0 0 22 22" aria-hidden="true">
          <circle cx="11" cy="11" r="11" fill="var(--teal)"/>
          <rect x="5.5" y="7" width="11" height="8" rx="1" fill="#fff"/>
          <path d="M5.8 7.5 11 11.5l5.2-4" fill="none" stroke="var(--teal)" stroke-width="1"/>
        </svg>nell@silverkettlephotography.co.uk
      </li>
      <li class="contact-item">
        <svg class="contact-icon" viewBox="0 0 22 22" aria-hidden="true">
          <circle cx="11" cy="11" r="11" fill="var(--teal)"/>
          <g fill="none" stroke="#fff" stroke-width="1.2">
            <circle cx="11" cy="11" r="5.5"/>
            <ellipse cx="11" cy="11" rx="2.4" ry="5.5"/>
            <path d="M5.5 11h11"/>
          </g>
        </svg>silverkettlephotography.co.uk
      </li>
      <li class="contact-item">
        <svg class="contact-icon" viewBox="0 0 22 22" aria-hidden="true"><circle cx="11" cy="11" r="11" fill="var(--teal)"/></svg>@silverkettlephotography
      </li>
      <li class="contact-item">
        <svg class="contact-icon" viewBox="0 0 22 22" aria-hidden="true"><circle cx="11" cy="11" r="11" fill="var(--teal)"/></svg>pinnestry.com/silverkettlepho
      </li>
      <li class="contact-item">
        <svg class="contact-icon" viewBox="0 0 22 22" aria-hidden="true"><circle cx="11" cy="11" r="11" fill="var(--teal)"/></svg>@silverkettle_photography
      </li>
    </ul>

    <p class="tagline">family portraiture, captured with love</p>
  </section>
</body>
</html>
```